Business Card & Logo Design

Originally the brief was for a card only - I now think it's probably better to include a logo design as well. PLease add $200 to the Budget of $210, Apologies for the inconvenience for thaos that have already submitted designs.

Lamp And Harbor Studios Pty Ltd is a video/dvd/ production company. Primarily corporate medium to high end. It's a one man operation that's been in business 20 years.

The name " Lamp and Harbor" is a primarily a reference to Lucien Marbeck film that's about film making. Shooting "Lamp and harbor" is also a technique employed by cinematographers to make scenes shot in daylight look like night.

See the design emphasising blue day/night tones but open to other ideas.

Main Text can either be Lamp and Harbor Studios or Lamp And Harbor.
Updates

Many thanks to all designers who submitted ideas for this brief.

Choosing between the designs was very difficult indeed.

I wish everyone the best and may the next job be yours!

Walter

Industry/Entity Type

Business

Requirements
Must have
• Text for card:
In Larger Print
Lamp And Harbor Studios or Lamp And Harbor
Walter Brenic
In Smaller Print
Lamp And Harbor Studios Pty Ltd.
17 Calder Lane
Ashby Vale, VIC, 3152
P: 9734 2061
m: 0417 385 902
e: walterbrenic@examplemail.net

```html
<!DOCTYPE html>
<html lang="en">
<head>
<meta charset="utf-8">
<title>Lamp and Harbor Studios – Business Card</title>
<link href="https://fonts.googleapis.com/css2?family=Questrial&display=swap" rel="stylesheet">
<style>
  :root {
    --page: #ffffff;
    --board-top: #d9dadc;
    --board-mid: #f1f1f2;
    --board-bottom: #dcdddf;
    --brand-blue: #1b5d94;
    --brand-blue-deep: #10508a;
    --brand-blue-light: #1a8fcd;
    --ink: #333333;
    --card-white: #ffffff;
    --card-grey: #eeeff1;
    --rule: #ffffff;
  }
  html, body {
    margin: 0;
    padding: 0;
    width: 1168px;
    height: 1200px;
    overflow: hidden;
    background: var(--page);
    font-family: "Questrial", "Century Gothic", sans-serif;
  }
  .board {
    position: absolute;
    left: 14px;
    top: 14px;
    width: 1140px;
    height: 1172px;
    border-radius: 50px;
    background: radial-gradient(ellipse at 50% 45%, var(--board-mid) 0%, var(--board-top) 80%, var(--board-bottom) 100%);
    box-shadow: inset 0 0 0 1px #cfd0d2;
  }
  .side-label {
    position: absolute;
    font-size: 25px;
    color: var(--ink);
  }
  .side-rule {
    position: absolute;
    height: 2px;
    background: var(--rule);
  }
  .card {
    position: absolute;
    width: 596px;
    height: 360px;
    box-shadow: 4px 6px 10px rgba(0,0,0,0.35);
  }
  .card--front {
    left: 215px;
    top: 266px;
    background: linear-gradient(120deg, var(--card-white) 0%, var(--card-grey) 100%);
  }
  .card--back {
    left: 438px;
    top: 670px;
    width: 589px;
    background: linear-gradient(90deg, var(--brand-blue-deep) 0%, var(--brand-blue-deep) 35%, var(--brand-blue-light) 100%);
  }
  .brand-mark {
    position: absolute;
    display: flex;
    align-items: center;
    gap: 14px;
  }
  .brand-mark__square {
    width: 56px;
    height: 56px;
    border-radius: 8px;
    flex: none;
  }
  .brand-mark__name {
    font-size: 30px;
    line-height: 1.1;
    letter-spacing: 0.3px;
    white-space: nowrap;
  }
  .card--front .brand-mark { left: 34px; top: 52px; }
  .card--front .brand-mark__square { background: var(--brand-blue); }
  .card--front .brand-mark__name { color: var(--brand-blue); }
  .card--back .brand-mark { left: 50%; top: 128px; transform: translateX(-50%); }
  .card--back .brand-mark__square { background: var(--card-white); }
  .card--back .brand-mark__name { color: var(--card-white); }
  .company {
    position: absolute;
    right: 27px;
    top: 80px;
    text-align: right;
  }
  .company__name {
    font-size: 23px;
    color: var(--brand-blue);
    letter-spacing: 0.3px;
  }
  .company__legal {
    font-size: 18px;
    color: var(--ink);
    margin-top: 1px;
  }
  .address {
    position: absolute;
    left: 34px;
    top: 212px;
    font-size: 17px;
    line-height: 25px;
    color: var(--ink);
  }
  .contact {
    position: absolute;
    right: 27px;
    top: 198px;
    text-align: right;
  }
  .contact__person {
    font-size: 30px;
    color: var(--brand-blue);
    margin-bottom: 8px;
  }
  .contact__line {
    font-size: 17px;
    line-height: 28px;
    color: var(--ink);
  }
  .contact__key {
    color: var(--brand-blue);
    font-weight: 700;
  }
</style>
</head>
<body>
  <div class="board"></div>

  <div class="side-rule" style="left:14px; top:626px; width:201px;"></div>
  <div class="side-label" style="left:148px; top:594px;">front</div>

  <div class="side-rule" style="left:227px; top:1025px; width:211px;"></div>
  <div class="side-label" style="left:360px; top:991px;">back</div>

  <section class="card card--front" aria-label="Business card front">
    <div class="brand-mark">
      <span class="brand-mark__square"></span>
      <span class="brand-mark__name">Lamp and<br>Harbor</span>
    </div>
    <div class="company">
      <div class="company__name">LAMP AND HARBOR</div>
      <div class="company__legal">Studios Pty Ltd.</div>
    </div>
    <div class="address">
      17 Calder Lane<br>
      Ashby Vale, VIC, 3152
    </div>
    <div class="contact">
      <div class="contact__person">Walter Brenic</div>
      <div class="contact__line"><span class="contact__key">P</span> : 9734 2061</div>
      <div class="contact__line"><span class="contact__key">M</span> : 0417 385 902</div>
      <div class="contact__line"><span class="contact__key">E</span> : walterbrenic@examplemail.net</div>
    </div>
  </section>

  <section class="card card--back" aria-label="Business card back">
    <div class="brand-mark">
      <span class="brand-mark__square"></span>
      <span class="brand-mark__name">Lamp and<br>Harbor</span>
    </div>
  </section>
</body>
</html>
```